Membership card Design

Hi I need a new membership card design for a social University club located in New Zealand. Our club name is called Maple Crest Society (MCSOC) and we provide a social hub for international students from Asia to meet local students. We are a non-profit organization that organizes activities such as paintball, ski trips, parties and day trips for our members. We need designs that look more like a membership card than a name card because we will be giving them to our members as a proof of membership. We would prefer a design that is simple in the front and with our club details, contacts and a place to write down a membership number on the back. We would like our card to have designs using the colours red, black, grey and orange. The design must incoporate the logo attached in this project. If possible, we would like the flower in the Hong Kong Flag to be incoporated in the design. The final design must look more like a membership card than a name card and communicate professionalism and high quality.

Target Market(s)

University Students

Industry/Entity Type

Non-Profit

Requirements
Must have
• The design must include:

The logo of our club
Our facebook page details: www.friendspage.example/maplecrest.soc
Our email: maplecrestsoc@mailbox.example
A place behind the card to print membership numbers.

```html
<!DOCTYPE html>
<html lang="en">
<head>
<meta charset="utf-8">
<title>Maple Crest Society Membership Card</title>
<link rel="stylesheet" href="https://fonts.googleapis.com/css2?family=Gelasio:ital,wght@0,400;0,700;1,700&display=swap">
<style>
  :root {
    --page: #ffffff;
    --card-black: #050505;
    --brand-red: #e0241b;
    --ink: #111111;
    --paper: #ffffff;
    --band: #000000;
    --white: #ffffff;
  }
  * { margin: 0; padding: 0; box-sizing: border-box; }
  html, body {
    width: 828px; height: 1200px; overflow: hidden;
    background: var(--page);
    font-family: "Gelasio", Georgia, serif;
  }
  .canvas { position: relative; width: 828px; height: 1200px; }

  .card-front {
    position: absolute; left: 14px; top: 6px; width: 800px; height: 578px;
    background: var(--card-black); overflow: hidden;
    box-shadow: 0 4px 10px rgba(0,0,0,0.35);
  }
  .card-front .glow {
    position: absolute; inset: 0;
    background: radial-gradient(circle 360px at 540px 260px, #ff1a1a 0%, #c40a0e 30%, #4a0305 65%, #050505 100%);
  }
  .member-photo {
    position: absolute; left: 30px; top: 50px; width: 222px; height: 236px;
    background: var(--paper);
    display: flex; justify-content: center; padding-top: 26px;
    font-size: 17px; color: var(--ink);
  }
  .member-name {
    position: absolute; left: 318px; top: 84px;
    color: var(--white); font-weight: 700; font-size: 44px; line-height: 1;
  }
  .member-year {
    position: absolute; left: 318px; top: 160px;
    color: var(--white); font-weight: 700; font-size: 32px; line-height: 1;
  }
  .club-mark {
    position: absolute; left: 22px; top: 470px;
    display: flex; align-items: center; gap: 10px;
  }
  .club-mark .dot {
    width: 46px; height: 46px; border-radius: 50%; background: var(--brand-red);
  }
  .club-mark .wordmark {
    color: var(--brand-red); font-weight: 700; font-size: 34px; letter-spacing: 0.5px;
  }

  .card-back {
    position: absolute; left: 14px; top: 612px; width: 800px; height: 578px;
    background: var(--paper); overflow: hidden;
    box-shadow: 0 4px 12px rgba(0,0,0,0.35);
  }
  .certify {
    position: absolute; left: 0; right: 0; top: 88px;
    text-align: center; font-size: 25px; line-height: 1.15; color: var(--ink);
  }
  .officer { position: absolute; top: 220px; width: 300px; text-align: center; color: var(--ink); white-space: nowrap; }
  .officer.president { left: 50px; }
  .officer.vice { left: 460px; }
  .officer .signature {
    display: inline-block; font-weight: 700; font-size: 18px; transform: rotate(-6deg);
    margin-bottom: 62px;
  }
  .officer .name { font-weight: 700; font-size: 20px; line-height: 1.1; }
  .officer .role { font-size: 14px; }

  .info-band {
    position: absolute; left: 0; right: 0; bottom: 0; height: 160px;
    background: var(--band); color: var(--white);
  }
  .band-acronym {
    position: absolute; left: 22px; top: 26px; font-size: 52px; line-height: 1;
  }
  .membership-number {
    position: absolute; left: 22px; top: 102px; font-weight: 700; font-style: italic; font-size: 22px;
  }
  .membership-number .line {
    display: inline-block; width: 160px; border-bottom: 2px solid var(--white); margin-left: 8px;
  }
  .contacts {
    position: absolute; right: 22px; top: 50px; text-align: left; font-size: 24px; line-height: 1.1;
  }
</style>
</head>
<body>
<div class="canvas">

  <section class="card-front">
    <div class="glow" aria-hidden="true"></div>
    <div class="member-photo">Picture of member</div>
    <h1 class="member-name">Name of Member</h1>
    <p class="member-year">Year joined</p>
    <div class="club-mark">
      <span class="dot"></span>
      <span class="wordmark">MAPLE CREST SOC</span>
    </div>
  </section>

  <section class="card-back">
    <p class="certify">This certifies that the owner of this card is a bonafide<br>member of the Maple Crest Society.</p>
    <div class="officer president">
      <span class="signature">signature</span>
      <p class="name">Name of President</p>
      <p class="role">President</p>
    </div>
    <div class="officer vice">
      <span class="signature">signature</span>
      <p class="name">Name of Vice President</p>
      <p class="role">Vice President</p>
    </div>
    <div class="info-band">
      <p class="band-acronym">MCSOC</p>
      <p class="membership-number">Membership #<span class="line"></span></p>
      <div class="contacts">
        <p>www.friendspage.example/maplecrest.soc</p>
        <p>maplecrestsoc@mailbox.example</p>
      </div>
    </div>
  </section>

</div>
</body>
</html>
```